Traffic product supplier - Temporary Raised Pavement Markers

We need a flyer design that will grab the customer's eye to the product (TRPMs) and entice curiosity to the business. Showing 1 product but promoting other products. The following information should be included:
- Logo (attached)
- Sale Product image (Temporary Road Pavement Marker AKA Press and Holds)
- Product wording (attached word document)

Happy for you to add/amend wording for grammatical purpose and other images that show it is a sale flyer.

Background on KLV - We are a thermoplastic manufacturer for road markings and traffic product supplier. KLV specializes in producing high quality hotmelt thermoplastic that meet Australian Standard AS4049.2. We are able to produce other specifications as required by the customer.

Would like the colour scheme to be similar to the logo.

If you need more information let me know.

Target Market(s)

Asphalt industry / road builders

Font styles to use
Serif
Sans Serif

Requirements
Must have
• - Kelvoro Lane Ventures (My company name)
- Contact details:
- 02 8417 2530
- marcus.t@klvsupplyco.com.au
- info@klvsupplyco.com.au
-www.klvmtq.com

- Attached images.
-Title (Temporary Road Pavement Markers)

```html
<!DOCTYPE html>
<html lang="en">
<head>
<meta charset="utf-8">
<title>KLV – Road Marking Products Flyer</title>
<link href="https://fonts.googleapis.com/css2?family=Anton&family=Montserrat:wght@400;500;600;700&display=swap" rel="stylesheet">
<style>
  :root{
    --blue:#1f6bb3;
    --blue-deep:#1a5c9c;
    --yellow:#e6dc23;
    --slate:#2e3b3c;
    --ink:#333;
    --grey-text:#6d6d6d;
    --tile:#ececec;
    --page:#ffffff;
    --backdrop:#f2f2f2;
  }
  *{margin:0;padding:0;box-sizing:border-box}
  html,body{width:1200px;height:2605px;overflow:hidden;background:var(--backdrop)}
  .stage{position:relative;width:1200px;height:2605px}
  .flyer{
    position:absolute;left:47px;top:520px;width:790px;height:1118px;
    transform:scale(1.4);transform-origin:0 0;
    background:var(--page);overflow:hidden;font-family:'Montserrat',sans-serif;
    box-shadow:0 6px 22px rgba(0,0,0,.18);
  }
  .abs{position:absolute}
  .hero-art{position:absolute;left:0;top:0}
  .brand{position:absolute;left:85px;top:30px;display:flex;align-items:center;gap:10px}
  .brand-square{width:22px;height:22px;background:var(--blue)}
  .brand-name{font-family:'Montserrat',sans-serif;font-weight:700;font-size:44px;color:var(--blue);letter-spacing:2px;line-height:1}
  .headline{position:absolute;left:57px;top:168px;font-family:'Anton',sans-serif;font-size:47px;line-height:51px;color:#fff;letter-spacing:.5px}
  .headline .accent{color:var(--yellow)}
  .section-title{position:absolute;top:500px;font-size:19px;font-weight:400;color:#333;letter-spacing:.3px}
  .section-title b{color:var(--blue);font-weight:700}
  .section-body{position:absolute;top:538px;width:318px;font-size:12.6px;line-height:16px;color:var(--grey-text)}
  .card{position:absolute;top:680px;width:218px;height:210px}
  .card-tab{position:absolute;left:0;top:0;width:38px;height:10px;background:var(--yellow)}
  .card-rule{position:absolute;left:0;top:0;width:200px;height:2px;background:var(--yellow)}
  .card-head{position:absolute;left:0;top:8px;width:218px;height:52px;background:var(--blue);color:#fff;font-weight:700;font-size:16.5px;padding:20px 0 0 18px}
  .card-photo{position:absolute;left:0;top:60px;width:218px;height:146px;background:linear-gradient(180deg,#f1f1f1,#e4e4e4)}
  .bullets{position:absolute;top:918px;list-style:none;font-weight:600;font-size:15.5px;line-height:19px;color:#2a2a2a}
  .bullets li{position:relative;padding-left:22px;margin-bottom:9px}
  .bullets li::before{content:"";position:absolute;left:0;top:5px;width:9px;height:9px;border-radius:50%;background:var(--yellow)}
  .footer-art{position:absolute;left:0;top:1040px}
  .contact{position:absolute;color:#fff;font-size:18px;line-height:21px}
  .contact .phone{font-weight:700;letter-spacing:.5px}
  .web{position:absolute;top:1075px;color:#fff;font-size:13px}
</style>
</head>
<body>
<div class="stage">
  <div class="flyer">
    <svg class="hero-art" width="790" height="480" viewBox="0 0 790 480">
      <defs>
        <linearGradient id="skyRoad" x1="0" y1="0" x2="0" y2="1">
          <stop offset="0" stop-color="#2f68ad"/>
          <stop offset=".35" stop-color="#7fa3c8"/>
          <stop offset=".55" stop-color="#3f4c55"/>
          <stop offset="1" stop-color="#4a4a4f"/>
        </linearGradient>
      </defs>
      <g role="img" aria-label="Photo of a city skyline at dusk with light trails on a highway">
        <polygon points="305,0 790,0 790,455 490,455 345,110 255,110" fill="url(#skyRoad)"/>
      </g>
      <polygon points="0,120 330,120 480,455 0,455" fill="var(--blue)"/>
      <polyline points="0,110 322,110 488,455" fill="none" stroke="var(--yellow)" stroke-width="2"/>
      <polygon points="0,457 497,457 485,472 0,472" fill="var(--yellow)"/>
      <polygon points="535,457 790,457 790,472 523,472" fill="var(--blue)"/>
    </svg>

    <div class="brand">
      <span class="brand-square"></span>
      <span class="brand-name">KLV</span>
    </div>

    <h1 class="headline">HIGH<br>STANDARD<br>QUALITY ROAD<br><span class="accent">MARKING<br>PRODUCTS</span></h1>

    <h2 class="section-title" style="left:50px">USE/GENERAL <b>DESCRIPTION:</b></h2>
    <p class="section-body" style="left:52px">Temporary road pavement markers, also known as press ‘n’ holds, are a great short-term solution to mark asphalt and pavements before permanent line marking takes place. They provide a way to delineate lanes and edges before the permanent longitudinal line marking process takes place.</p>

    <h2 class="section-title" style="left:393px">PRODUCT <b>DESCRIPTION:</b></h2>
    <p class="section-body" style="left:395px">TRPMs or press ‘n’ holds are available in yellow or white and come with a Class 1A reflective strip applied to tough high impact plastic. They are an economical solution for making newly laid roads safer. An easy to remove clear cover protects the reflective film during sealing and is easily ripped off afterwards.</p>

    <div class="card" style="left:55px">
      <div class="card-rule"></div><div class="card-tab"></div>
      <div class="card-head">Temp RPM - Yellow</div>
      <div class="card-photo" role="img" aria-label="Temporary road marker with red reflective strip"></div>
    </div>
    <div class="card" style="left:288px">
      <div class="card-rule"></div><div class="card-tab"></div>
      <div class="card-head">Temp RPM - Yellow</div>
      <div class="card-photo" role="img" aria-label="Yellow temporary road marker" style="background:linear-gradient(180deg,#f1f1f1,#e4e4e4)"></div>
    </div>
    <div class="card" style="left:521px">
      <div class="card-rule"></div><div class="card-tab"></div>
      <div class="card-head">Temp RPM - White</div>
      <div class="card-photo" role="img" aria-label="White temporary road marker with reflective strip"></div>
    </div>

    <ul class="bullets" style="left:53px;width:200px">
      <li>Dimensions:<br>100 mm long x 50 mm high x 25 mm wide</li>
    </ul>
    <ul class="bullets" style="left:293px;width:210px">
      <li>Double sided Class 1A Reflective</li>
      <li>Clear cover for reflective protection</li>
    </ul>
    <ul class="bullets" style="left:520px;width:230px">
      <li>Available in all white, and red (reflective strip)</li>
      <li>and white, all yellow and all blue</li>
    </ul>

    <svg class="footer-art" width="790" height="78" viewBox="0 0 790 78">
      <polygon points="0,4 392,4 360,78 0,78" fill="var(--slate)"/>
      <polygon points="395,18 790,18 790,78 358,78" fill="var(--blue)"/>
      <polyline points="790,24 402,24 380,72" fill="none" stroke="#8fb6de" stroke-width="1"/>
      <circle cx="523" cy="18" r="11" fill="var(--yellow)"/>
      <rect x="518" y="13" width="10" height="8" rx="1" fill="none" stroke="var(--blue)" stroke-width="1.5"/>
      <circle cx="682" cy="18" r="11" fill="var(--yellow)"/>
      <circle cx="682" cy="18" r="5.5" fill="none" stroke="var(--blue)" stroke-width="1.5"/>
      <line x1="676.5" y1="18" x2="687.5" y2="18" stroke="var(--blue)" stroke-width="1.2"/>
      <path d="M57,36 q0,10 10,10 l2,-3 -3,-2 -2,2 q-4,-2 -5,-5 l2,-2 -2,-3 z" fill="var(--yellow)"/>
      <rect x="57" y="53" width="10" height="8" rx="1" fill="none" stroke="var(--yellow)" stroke-width="1.5"/>
    </svg>
    <div class="contact" style="left:84px;top:1063px">
      <div class="phone">02 8417 2530</div>
      <div>marcus.t@klvsupplyco.com.au</div>
    </div>
    <div class="web" style="left:437px">info@klvsupplyco.com.au</div>
    <div class="web" style="left:632px">www.klvmtq.com</div>
  </div>
</div>
</body>
</html>
```